Desktop publishing rework of financial advisor's corporate marketing brochure

We are a financial and strategic business consultancy to corporate clients in healthcare/ pharmaceuticals. We previously had a very "wordy" slide presentation which we now thinned down to a few messages. We have created mockups of the layouts for the pages. We have also 95% finalized all wording for the pages. What we need is redesign proposals for all of the pages 1, 2, 4, 5, 6. These proposals should reflect the current layout/ arrangement of objects; they should be much more professional and generally "better looking" than what we currently have. They shall replace existing graphics with better-looking more appropriate ones.
Many thanks all

Requirements
Must have
• Use the PPT file shared below as basis

```html
<!DOCTYPE html>
<html lang="en">
<head>
<meta charset="utf-8">
<title>Ashgrove Partners – Brochure Pages</title>
<link href="https://fonts.googleapis.com/css2?family=Roboto:wght@400;500;700&family=Source+Serif+4:wght@400;600;700&display=swap" rel="stylesheet">
<style>
:root{
  --bg:#e9eaeb;
  --white:#ffffff;
  --blue:#1aa3d9;
  --blue-soft:#7cc8ea;
  --navy:#0b4a8d;
  --ink:#1c1f24;
  --grey:#9b9b9b;
  --grey-light:#c9cbcd;
  --text:#222428;
}
*{box-sizing:border-box;margin:0;padding:0}
html,body{width:1200px;height:4000px;overflow:hidden;background:var(--bg)}
body{position:relative;font-family:"Source Serif 4",Georgia,serif;color:var(--text)}
.slide{position:absolute;left:328px;width:545px;height:411px;background:var(--white);box-shadow:0 2px 8px rgba(0,0,0,.12);overflow:hidden}
.abs{position:absolute}
.title{position:absolute;left:37px;top:26px;font-size:21px;font-weight:700;line-height:1.25;color:var(--ink)}
.title .accent{color:var(--blue)}
.wordmark{font-family:"Source Serif 4",Georgia,serif;font-weight:400;color:var(--ink);letter-spacing:3px;text-align:center}
.foot-mark{position:absolute;left:28px;top:366px;font-size:12px;letter-spacing:2px;color:var(--ink)}
.foot-url{position:absolute;right:28px;top:378px;width:129px;height:11px;border-radius:6px;background:var(--ink);color:var(--white);font-family:Roboto,Arial,sans-serif;font-size:7px;line-height:11px;text-align:center}
/* cover */
.cover-mark{position:absolute;left:0;right:0;top:96px;font-size:26px}
.cover-band{position:absolute;left:0;top:199px;width:100%;height:212px;background:linear-gradient(180deg,#23272d,#15181c)}
.cover-line{position:absolute;left:0;top:190px;width:100%;height:5px;background:var(--blue)}
.cover-name{position:absolute;left:0;right:0;top:240px;text-align:center;font-family:Roboto,Arial,sans-serif;font-size:23px;color:var(--white)}
.cover-tag{position:absolute;left:0;right:0;top:272px;text-align:center;font-size:46px;color:var(--blue)}
.cover-url{position:absolute;left:170px;top:355px;width:205px;height:22px;border-radius:11px;background:var(--blue);color:var(--white);font-family:Roboto,Arial,sans-serif;font-weight:700;font-size:11px;line-height:22px;text-align:center}
/* stats */
.stat{position:absolute;width:144px;height:121px;border-radius:10px;overflow:hidden;text-align:center}
.stat-top{height:48px;background:linear-gradient(180deg,#2a2e34,#14171b);color:var(--white);font-size:26px;line-height:52px}
.stat-bot{height:73px;background:var(--blue);color:var(--white);font-size:15px;line-height:1.2;padding-top:10px}
/* logo wall */
.wall{position:absolute;left:51px;top:78px;width:444px;height:268px;border:2px solid var(--blue)}
.wall-badge{position:absolute;left:185px;top:60px;width:175px;height:30px;border:2px solid var(--blue);border-radius:15px;background:var(--white);font-size:12px;line-height:26px;text-align:center;letter-spacing:2px;color:var(--ink)}
.wall-grid{position:absolute;left:12px;top:34px;right:12px;bottom:14px;display:grid;grid-template-columns:repeat(5,1fr);align-items:center;justify-items:center;font-family:Roboto,Arial,sans-serif;font-size:10px;color:#55595e}
.wall-grid span:nth-child(3n){color:var(--blue)}
.wall.faint .wall-grid{opacity:.5}
/* pills */
.pill{position:absolute;height:26px;border-radius:13px;font-size:10px;line-height:26px;text-align:center;color:var(--white)}
.label{position:absolute;text-align:center;font-size:17px;line-height:1.2;font-weight:600;color:var(--ink)}
.label .accent{color:var(--blue)}
.cap{position:absolute;font-size:9px;color:var(--blue);text-align:center}
</style>
</head>
<body>

<!-- Page 1: cover -->
<section class="slide" style="top:116px">
  <div class="wordmark cover-mark">ASHGROVE PARTNERS</div>
  <div class="cover-line"></div>
  <div class="cover-band"></div>
  <div class="cover-name">ASHGROVE PARTNERS</div>
  <div class="cover-tag">Beyond Advisory.</div>
  <div class="cover-url">www.ashgrovepartners.com</div>
</section>

<!-- Page 2: key figures -->
<section class="slide" style="top:582px">
  <h1 class="title"><span class="accent">Healthcare-Focused Advisor</span><br>Founded by Former Stonebridge Team</h1>
  <div class="stat" style="left:37px;top:99px"><div class="stat-top">15</div><div class="stat-bot">Senior<br>Professionals</div></div>
  <div class="stat" style="left:197px;top:99px"><div class="stat-top">&gt;$150bn</div><div class="stat-bot">Transacted<br>Deal Value</div></div>
  <div class="stat" style="left:357px;top:99px"><div class="stat-top">15</div><div class="stat-bot">Transacted<br>Deal Value</div></div>
  <div class="stat" style="left:37px;top:236px"><div class="stat-top">25yrs</div><div class="stat-bot">Average<br>Experience</div></div>
  <div class="stat" style="left:197px;top:236px"><div class="stat-top">&gt;100</div><div class="stat-bot">Individual<br>Transaction</div></div>
  <div class="stat" style="left:357px;top:236px"><div class="stat-top">&gt;20</div><div class="stat-bot">C-Suite<br>Positions Held</div></div>
  <div class="foot-mark">ASHGROVE PARTNERS</div>
  <div class="foot-url">www.ashgrovepartners.com</div>
</section>

<!-- Page 3: expertise -->
<section class="slide" style="top:1048px">
  <h1 class="title"><span class="accent">Deep Complementary</span> Senior Expertise</h1>
  <div class="wall">
    <div class="wall-grid">
      <span>Corvane Group</span><span>Halden Bank</span><span>Meridex</span><span>Lystra Bio</span><span>Norvel</span>
      <span>Pallas Health</span><span>Quintera</span><span>Renvo</span><span>Sorrel Pharma</span><span>Tavira</span>
      <span>Umbra Labs</span><span>Veltis</span><span>Wexford Bio</span><span>Xandor</span><span>Yarrow Med</span>
      <span>Zentis</span><span>Ardent Rx</span><span>Bexley</span><span>Calder</span><span>Dunmore</span>
    </div>
  </div>
  <svg class="abs" style="left:0;top:0" width="545" height="411" aria-hidden="true">
    <g stroke="#1aa3d9" stroke-width="2" fill="none"><path d="M100 75H180M173 70l7 5-7 5"/><path d="M445 75H365M372 70l-7 5 7 5"/></g>
  </svg>
  <div class="wall-badge">ASHGROVE</div>
  <div class="foot-mark">ASHGROVE PARTNERS</div>
  <div class="foot-url">www.ashgrovepartners.com</div>
</section>

<!-- Page 4: expertise, faded variant -->
<section class="slide" style="top:1514px">
  <h1 class="title"><span class="accent">Deep Complementary</span> Senior Expertise</h1>
  <div class="wall faint">
    <div class="wall-grid">
      <span>Corvane Group</span><span>Halden Bank</span><span>Meridex</span><span>Lystra Bio</span><span>Norvel</span>
      <span>Pallas Health</span><span>Quintera</span><span>Renvo</span><span>Sorrel Pharma</span><span>Tavira</span>
      <span>Umbra Labs</span><span>Veltis</span><span>Wexford Bio</span><span>Xandor</span><span>Yarrow Med</span>
      <span>Zentis</span><span>Ardent Rx</span><span>Bexley</span><span>Calder</span><span>Dunmore</span>
    </div>
  </div>
  <svg class="abs" style="left:0;top:0" width="545" height="411" aria-hidden="true">
    <g stroke="#1aa3d9" stroke-width="2" fill="none"><path d="M100 75H180M173 70l7 5-7 5"/><path d="M445 75H365M372 70l-7 5 7 5"/></g>
  </svg>
  <div class="wall-badge">ASHGROVE</div>
  <div class="foot-mark">ASHGROVE PARTNERS</div>
  <div class="foot-url">www.ashgrovepartners.com</div>
</section>

<!-- Page 5: approach -->
<section class="slide" style="top:1980px">
  <h1 class="title" style="left:28px"><span class="accent">Unique Approach to</span> Delivering Client Success</h1>
  <div class="pill" style="left:42px;top:75px;width:175px;background:var(--blue)">Seamless Integration of Disciplines</div>
  <div class="pill" style="left:275px;top:75px;width:236px;background:var(--ink)">Successful Transactions &amp; Corporate Evolutions</div>
  <svg class="abs" style="left:0;top:0" width="545" height="411">
    <g transform="translate(124 225)">
      <path d="M0 0L0-101A101 101 0 0 1 87.5 50.5Z" fill="#1aa3d9"/>
      <path d="M0 0L87.5 50.5A101 101 0 0 1-87.5 50.5Z" fill="#9b9b9b"/>
      <path d="M0 0L-87.5 50.5A101 101 0 0 1 0-101Z" fill="#0b4a8d"/>
      <circle cx="-43" cy="-36" r="17" fill="#fff"/><circle cx="48" cy="-31" r="17" fill="#fff"/><circle cx="-3" cy="53" r="17" fill="#fff"/>
      <g font-family="Source Serif 4,Georgia,serif" font-weight="700" font-size="14" fill="#1c1f24" text-anchor="middle">
        <text x="-43" y="-31">01</text><text x="48" y="-26">02</text><text x="-3" y="58">03</text>
      </g>
      <g font-family="Source Serif 4,Georgia,serif" font-size="9" fill="#fff">
        <text x="5" y="-68">Transaction</text><text x="-88" y="17">Strategy</text><text x="20" y="57">Management</text>
      </g>
    </g>
    <text x="274" y="220" font-family="Source Serif 4,Georgia,serif" font-size="12" text-anchor="middle" fill="#1c1f24">Consolidated</text>
    <text x="274" y="233" font-family="Source Serif 4,Georgia,serif" font-size="12" text-anchor="middle" fill="#1c1f24">Output</text>
    <path d="M313 210H385V202L402 219L385 236V228H313Z" fill="#1aa3d9"/>
    <text x="360" y="222" font-family="Source Serif 4,Georgia,serif" font-size="10" text-anchor="middle" fill="#fff">Enable and Pursue</text>
    <circle cx="457" cy="219" r="59" fill="#1c1f24"/>
    <circle cx="457" cy="219" r="48" fill="#1aa3d9"/>
    <circle cx="457" cy="219" r="30" fill="#fff"/>
    <circle cx="457" cy="219" r="23" fill="#1c1f24"/>
    <circle cx="457" cy="219" r="9" fill="none" stroke="#fff" stroke-width="3"/>
  </svg>
  <div class="foot-mark">ASHGROVE PARTNERS</div>
  <div class="foot-url">www.ashgrovepartners.com</div>
</section>

<!-- Page 6: enhanced insight -->
<section class="slide" style="top:2446px">
  <h1 class="title" style="left:28px"><span class="accent">Outsourced Solution Delivery Office</span><br>&nbsp;– Enhanced Insight</h1>
  <svg class="abs" style="left:0;top:0" width="545" height="411">
    <path d="M144 180H213M331 180H393" stroke="#1aa3d9" stroke-dasharray="2 3"/>
    <g fill="none" stroke-width="3">
      <circle cx="85" cy="180" r="59" stroke="#1aa3d9"/><circle cx="272" cy="180" r="59" stroke="#1aa3d9"/><circle cx="452" cy="180" r="59" stroke="#1aa3d9"/>
    </g>
    <g fill="#fff" stroke="#1c1f24" stroke-width="2.5">
      <circle cx="85" cy="180" r="51"/><circle cx="452" cy="180" r="51"/>
    </g>
    <circle cx="272" cy="180" r="51" fill="#4b8fb8" role="img" aria-label="Photo of a person looking through binoculars"/>
    <g stroke="#1c1f24" stroke-width="4" fill="none" stroke-linecap="round">
      <path d="M72 210H102M86 204L80 168M80 168L95 152M92 182A14 14 0 0 1 76 200"/>
    </g>
    <g fill="#9b9b9b"><circle cx="435" cy="170" r="6"/><path d="M425 192Q435 176 445 192Z"/></g>
    <path d="M452 180H462M462 165V195M462 165H472M462 180H472M462 195H472" stroke="#1c1f24" stroke-width="1.5" fill="none"/>
  </svg>
  <div class="label" style="left:25px;top:261px;width:120px"><span class="accent">Inward</span><br>Transactions</div>
  <div class="label" style="left:212px;top:261px;width:120px"><span class="accent">Senior</span><br>Management</div>
  <div class="label" style="left:392px;top:261px;width:120px"><span class="accent">Outward</span><br>Transactions</div>
  <div class="foot-mark">ASHGROVE PARTNERS</div>
  <div class="foot-url">www.ashgrovepartners.com</div>
</section>

<!-- Page 7: areas of work -->
<section class="slide" style="top:2912px">
  <h1 class="title" style="left:28px"><span class="accent">Outsourced Solution Delivery Office –</span><br>Areas of Work</h1>
  <svg class="abs" style="left:0;top:0" width="545" height="411">
    <polygon points="121,134 211,292 31,292" fill="#1aa3d9"/>
    <polygon points="334,134 512,134 423,292" fill="#1aa3d9"/>
    <g stroke="#fff" stroke-width="3">
      <path d="M30 173H212M30 212H212M30 251H212"/>
      <path d="M334 169H512M334 205H512M334 240H512"/>
    </g>
    <g font-family="Source Serif 4,Georgia,serif" font-size="9" fill="#fff" text-anchor="middle" font-weight="600">
      <text x="121" y="167">Identify</text><text x="121" y="199">Screen</text><text x="121" y="235">Review</text><text x="121" y="275">Transact</text>
      <text x="423" y="154">Plan</text><text x="423" y="190">Prepare</text><text x="423" y="225">Approach</text><text x="423" y="259">Execute</text>
    </g>
    <g transform="translate(272 197)">
      <path d="M0 0V-70A70 70 0 0 1 70 0Z" fill="#1aa3d9"/>
      <path d="M0 0H70A70 70 0 0 1 0 70Z" fill="#9b9b9b"/>
      <path d="M0 0V70A70 70 0 0 1-70 0Z" fill="#1aa3d9"/>
      <path d="M0 0H-70A70 70 0 0 1 0-70Z" fill="#9b9b9b"/>
      <g stroke="#fff" stroke-width="3"><path d="M0-72V72M-72 0H72"/></g>
      <g fill="#fff"><circle cx="0" cy="-35" r="8"/><circle cx="35" cy="0" r="8"/><circle cx="0" cy="35" r="8"/><circle cx="-35" cy="0" r="8"/></g>
      <g font-family="Source Serif 4,Georgia,serif" font-size="9" font-weight="700" fill="#1c1f24" text-anchor="middle">
        <text x="30" y="-20">Adjust</text><text x="42" y="3">Monitor</text><text x="-1" y="20">Implement</text><text x="-43" y="3">Strategize</text>
      </g>
    </g>
  </svg>
  <div class="cap" style="left:31px;top:305px;width:180px">Inward Transactions</div>
  <div class="cap" style="left:202px;top:305px;width:140px">Senior Management</div>
  <div class="cap" style="left:334px;top:305px;width:178px">Outward Transactions</div>
  <div class="foot-mark">ASHGROVE PARTNERS</div>
  <div class="foot-url">www.ashgrovepartners.com</div>
</section>

<!-- Page 8: global coverage -->
<section class="slide" style="top:3378px">
  <h1 class="title" style="left:28px"><span class="accent">Global</span> Coverage</h1>
  <div class="abs" style="left:68px;top:152px;width:427px;height:210px;border-radius:40px;background:radial-gradient(ellipse at center,#cfd1d3,#eef0f1 75%)" role="img" aria-label="Grey world map with office markers in North America and Europe"></div>
  <svg class="abs" style="left:0;top:0" width="545" height="411">
    <g fill="none" stroke-width="9">
      <circle cx="110" cy="113" r="43" stroke="#c9cbcd"/>
      <circle cx="110" cy="113" r="43" stroke="#1aa3d9" stroke-dasharray="230 270" transform="rotate(-90 110 113)"/>
      <circle cx="275" cy="113" r="43" stroke="#1aa3d9"/>
      <circle cx="435" cy="113" r="43" stroke="#1aa3d9"/>
    </g>
    <g font-family="Roboto,Arial,sans-serif" font-weight="700" font-size="24" fill="#1c1f24" text-anchor="middle">
      <text x="110" y="122">85%</text><text x="275" y="122">10%</text><text x="435" y="122">5%</text>
    </g>
    <g fill="#d9262c"><circle cx="158" cy="235" r="4"/><circle cx="150" cy="243" r="3"/><circle cx="253" cy="212" r="4"/><circle cx="259" cy="220" r="3"/></g>
    <rect x="240" y="188" width="30" height="16" rx="2" fill="#0b4a8d"/>
    <rect x="142" y="246" width="32" height="14" rx="2" fill="#0b4a8d"/>
  </svg>
  <div class="foot-mark">ASHGROVE PARTNERS</div>
  <div class="foot-url">www.ashgrovepartners.com</div>
</section>

</body>
</html>
```